Physiotherapiepraxis braucht Druckvorlage für Werbeanzeige
Zielgruppe
Dienstleistung im Gesundheitswesen als Physiotherapiepraxis.
Krankengymnastik, auch im häuslichen Bereich oder im Altersheim, und Massage sowie Wellnessanwendungen.
Zielgruppe sind primär Erwachsene, eingeschränkt auch Kinder.
Aufgabenstellung
Ich möchte eine Druckvorlage für eine Werbeanzeige, die ich immer mal wieder in verschiedenen Festschriften im dörflichen Bereich oder in einer regionalen Zeitschrift veröffentlichen kann.
Die Anzeige soll das Logo enthalten und die Anschrift der Praxis sowie die Telefonnummer und Adresse der Homepage.

```html
<!DOCTYPE html>
<html lang="de">
<head>
<meta charset="utf-8">
<title>Anzeigen Physiotherapie Carola Brandt</title>
<link rel="stylesheet" href="https://fonts.googleapis.com/css2?family=Source+Sans+3:wght@400;600;700&display=swap">
<style>
  :root {
    --gold: #d4b826;
    --green: #007a3d;
    --dark: #555555;
    --grey: #b0b0b0;
    --label: #6b6b6b;
    --white: #ffffff;
  }
  * { box-sizing: border-box; margin: 0; padding: 0; }
  html, body { width: 1200px; height: 846px; overflow: hidden; background: var(--white); }
  body { position: relative; font-family: "Source Sans 3", "Myriad Pro", Arial, sans-serif; }

  .section-label {
    position: absolute;
    font-size: 20px;
    font-weight: 400;
    color: var(--label);
    letter-spacing: 0.1px;
  }

  .ad { position: absolute; border: 2px solid var(--tone); background: var(--white); }
  .ad--gold { --tone: var(--gold); --name: var(--green); }
  .ad--green { --tone: var(--green); --name: var(--green); }
  .ad--grey { --tone: var(--dark); --name: var(--grey); }

  .ad__info {
    background: var(--tone);
    color: var(--white);
    font-size: 14px;
    line-height: 18.5px;
  }
  .ad__info strong { font-weight: 700; display: block; }
  .ad__info span { display: block; }

  .ad__brand {
    display: flex;
    align-items: center;
    justify-content: center;
    gap: 10px;
  }
  .brand__dot { width: 14px; height: 14px; border-radius: 50%; background: var(--name); flex: none; }
  .brand__name {
    color: var(--name);
    font-weight: 600;
    font-size: 21px;
    line-height: 25px;
    letter-spacing: 1.2px;
    text-align: left;
  }

  /* single column, 45 mm */
  .ad--single { top: 81px; width: 257px; height: 257px; display: flex; flex-direction: column; }
  .ad--single .ad__info { height: 137px; padding: 8px 13px 0; }
  .ad--single .gap { height: 4px; }
  .ad--single .ad__brand { flex: 1; }

  /* double column, 90 mm */
  .ad--double { left: 343px; width: 514px; height: 114px; display: flex; }
  .ad--double .ad__brand { width: 256px; }
  .ad--double .ad__info { flex: 1; padding: 9px 12px 0; line-height: 20.5px; }
</style>
</head>
<body>
  <p class="section-label" style="left:143px; top:42px;">Anzeigen 1-spaltig, 45 mm breit</p>

  <article class="ad ad--single ad--gold" style="left:142px;">
    <div class="ad__info">
      <strong>Praxis für Physiotherapie</strong>
      <strong>Carola Brandt</strong>
      <div class="gap"></div>
      <span>Lindenweg 7</span>
      <span>21493 Mühlenau</span>
      <div class="gap"></div>
      <span>Tel. 04155 482610</span>
      <strong>www.physiotherapie-muehlenau.de</strong>
    </div>
    <div class="ad__brand"><i class="brand__dot"></i><p class="brand__name">Carola Brandt<br>Physiotherapie</p></div>
  </article>

  <article class="ad ad--single ad--green" style="left:471px;">
    <div class="ad__info">
      <strong>Praxis für Physiotherapie</strong>
      <strong>Carola Brandt</strong>
      <div class="gap"></div>
      <span>Lindenweg 7</span>
      <span>21493 Mühlenau</span>
      <div class="gap"></div>
      <span>Tel. 04155 482610</span>
      <strong>www.physiotherapie-muehlenau.de</strong>
    </div>
    <div class="ad__brand"><i class="brand__dot"></i><p class="brand__name">Carola Brandt<br>Physiotherapie</p></div>
  </article>

  <article class="ad ad--single ad--grey" style="left:800px;">
    <div class="ad__info">
      <strong>Praxis für Physiotherapie</strong>
      <strong>Carola Brandt</strong>
      <div class="gap"></div>
      <span>Lindenweg 7</span>
      <span>21493 Mühlenau</span>
      <div class="gap"></div>
      <span>Tel. 04155 482610</span>
      <strong>www.physiotherapie-muehlenau.de</strong>
    </div>
    <div class="ad__brand"><i class="brand__dot"></i><p class="brand__name">Carola Brandt<br>Physiotherapie</p></div>
  </article>

  <p class="section-label" style="left:343px; top:384px;">Anzeigen 2-spaltig, 90 mm breit</p>

  <article class="ad ad--double ad--gold" style="top:422px;">
    <div class="ad__brand"><i class="brand__dot"></i><p class="brand__name">Carola Brandt<br>Physiotherapie</p></div>
    <div class="ad__info">
      <strong style="line-height:18px">Praxis für Physiotherapie</strong>
      <strong style="line-height:18px">Carola Brandt</strong>
      <span>Lindenweg 7, 21493 Mühlenau</span>
      <span>Tel. 04155 482610</span>
      <strong>www.physiotherapie-muehlenau.de</strong>
    </div>
  </article>

  <article class="ad ad--double ad--green" style="top:557px;">
    <div class="ad__brand"><i class="brand__dot"></i><p class="brand__name">Carola Brandt<br>Physiotherapie</p></div>
    <div class="ad__info">
      <strong style="line-height:18px">Praxis für Physiotherapie</strong>
      <strong style="line-height:18px">Carola Brandt</strong>
      <span>Lindenweg 7, 21493 Mühlenau</span>
      <span>Tel. 04155 482610</span>
      <strong>www.physiotherapie-muehlenau.de</strong>
    </div>
  </article>

  <article class="ad ad--double ad--grey" style="top:693px;">
    <div class="ad__brand"><i class="brand__dot"></i><p class="brand__name">Carola Brandt<br>Physiotherapie</p></div>
    <div class="ad__info">
      <strong style="line-height:18px">Praxis für Physiotherapie</strong>
      <strong style="line-height:18px">Carola Brandt</strong>
      <span>Lindenweg 7, 21493 Mühlenau</span>
      <span>Tel. 04155 482610</span>
      <strong>www.physiotherapie-muehlenau.de</strong>
    </div>
  </article>
</body>
</html>
```